RTW Gourmet Mushrooms web presence and site

The goal is to attract local buyers of fresh mushrooms and to both local and international buyers freeze dried mushrooms. Mushrooms grown will be oyster mushrooms (yellow, pink, blue, king), shiitake, lions main, chestnut, and more. My business will also be selling grow kits that help families who would like to grow there own mushrooms

Target Market(s)

Local restaurants, foodies and people seeking high quality fresh and freeze dried gourmet mushrooms

Coding

Coded - Design and coding required

Number of Pages Required

1 page

Font styles to use
Serif

Requirements
Must have
• Pictures of the various mushrooms grown along with the characteristics of each of the mushrooms. Recipes and cooking tips for the various mushrooms. There needs to be
1. Order forms with online payments
2. Feedback
3. Preorders for mushrooms that may be more seasonal
4.links to social media Facebook, LinkedIn, etc... I am not knowledgeable in this area
5. Contact Us link email, address, phone
6. About Us link explaining Peter Lindqvist & Moira Dunstable and a brief explanation about us and why we became Mushroom farmers
7. Descriptions of the various mushroom varieties grown and how they are best prepared and served
8. Why Freeze Drying mushrooms and the benefits of Freeze Drying over other methods of preservation.
Nice to have
• 1. Recipes and cooking tips for each of the mushrooms.
2. Weekly additional resources added to different pages
3. Q&A section
4. Food Blog with resources added weekly
5.

Flexibility with future expansion and growth is essential. I would like to have a growing site, not a stagnant site.
Should not have
• 1. Boring, bland presentation.
2. The web site is one to educate, promote the various mushrooms grown
3. No music, video or sound on the main pages but eventually a Vlog might be in the works.

I realize there is a lot of content requested but the content needs to attract buyers and to have the site a go to site for foodies

```html
<!DOCTYPE html>
<html lang="en">
<head>
<meta charset="utf-8">
<title>RTW Gourmet Mushrooms</title>
<link href="https://fonts.googleapis.com/css2?family=Playfair+Display:wght@400;500&family=Lora:wght@400&family=Montserrat:wght@400;500;600&family=Yesteryear&display=swap" rel="stylesheet">
<style>
:root{
  --accent:#b97a4c;
  --button:#a46a3f;
  --topbar:#c48c5e;
  --ink:#2b1e16;
  --body:#4a403a;
  --paper:#f6f5f3;
  --dark:#3a2416;
  --footer:#242322;
  --field:#3a3a3a;
}
*{box-sizing:border-box;margin:0;padding:0}
html,body{width:1200px;height:3817px;overflow:hidden}
body{position:relative;background:var(--paper);font-family:'Lora',serif;color:var(--body)}
.abs{position:absolute}
.script{font-family:'Yesteryear',cursive}
.serif-head{font-family:'Playfair Display',serif;font-weight:400;color:var(--ink)}
.sans{font-family:'Montserrat',sans-serif}
.btn{position:absolute;display:flex;align-items:center;justify-content:center;background:var(--button);color:#fff;font-family:'Montserrat',sans-serif;font-weight:600;font-size:14px;border-radius:3px;letter-spacing:.3px}

/* top bar */
.topbar{top:0;left:0;width:1200px;height:27px;background:var(--topbar);color:#fff;font-family:'Montserrat',sans-serif;font-size:14px}
.topbar .mail{left:114px;top:4px}
.topbar .links{left:660px;top:5px;display:flex;gap:0}
.topbar .links span{margin-right:40px}
.topbar .socials{left:972px;top:8px;display:flex;gap:21px}
.topbar .socials i{display:block;width:11px;height:11px;border-radius:50%;background:#fff}

/* header */
.header{top:27px;left:0;width:1200px;height:111px;background:#fafafa}
.brand{left:114px;top:28px;width:180px;font-family:'Playfair Display',serif;font-size:22px;line-height:26px;color:var(--dark)}
.nav{left:450px;top:55px;display:flex;font-family:'Montserrat',sans-serif;font-size:16px;color:var(--ink)}
.nav span{margin-right:44px}
.nav .active{color:var(--accent);border-bottom:2px solid var(--accent);padding-bottom:10px}
.cart{left:978px;top:48px;display:flex;align-items:center;gap:12px;font-family:'Montserrat',sans-serif;font-size:16px;color:var(--ink)}
.cart .ring{width:36px;height:36px;border-radius:50%;background:var(--accent);display:flex;align-items:center;justify-content:center}

/* hero */
.hero{top:138px;left:0;width:1200px;height:427px;background:radial-gradient(ellipse at 40% 40%,#8a5a34 0%,#5a3720 45%,#2e1b10 100%)}
.hero h1{position:absolute;left:0;width:1200px;top:138px;text-align:center;font-family:'Yesteryear',cursive;font-weight:400;font-size:96px;color:#fff;text-shadow:0 3px 10px rgba(0,0,0,.5)}
.down{left:568px;top:533px;width:64px;height:64px;border-radius:50%;background:var(--accent);display:flex;align-items:center;justify-content:center}

/* about */
.about-kicker{left:0;top:628px;width:1200px;text-align:center;font-size:34px;color:var(--accent)}
.about-title{left:0;top:670px;width:1200px;text-align:center;font-size:34px}
.about-text{left:158px;top:726px;width:886px;text-align:center;font-size:13.5px;line-height:24px}
.member .photo{width:203px;height:191px;border:6px solid #fff;box-shadow:0 0 0 1px #d8d8d8,0 2px 6px rgba(0,0,0,.12);background:linear-gradient(160deg,#cfcfcf,#8d8782)}
.member .name{font-family:'Playfair Display',serif;font-size:21px;color:var(--ink)}
.member .desc{font-size:13.5px;line-height:21px;width:240px}
.deco{background:linear-gradient(135deg,#e8ddd2,#a48a74)}

/* varieties */
.varieties{top:1096px;left:0;width:1200px;height:680px;background:radial-gradient(ellipse at 50% 50%,#4b3020 0%,#2f1c11 70%,#24150c 100%)}
.varieties .kicker{left:0;top:52px;width:1200px;text-align:center;font-size:32px;color:#d9a071}
.varieties .title{left:0;top:92px;width:1200px;text-align:center;font-size:36px;color:#fff}
.variety{position:absolute;width:220px;text-align:center}
.variety .pic{margin:0 auto;width:150px;height:150px;border-radius:40%}
.variety .label{margin-top:12px;font-family:'Yesteryear',cursive;font-size:28px;color:#fff}

/* benefits */
.prep-card{left:114px;top:1871px;width:422px;height:379px;border:3px solid #e1dedb;background:#f3f1ee}
.prep-card .kicker{left:30px;top:24px;font-size:30px;color:#8f8a86}
.prep-card h3{left:30px;top:66px;font-size:32px}
.prep-card p{left:30px;top:122px;width:365px;font-size:13.5px;line-height:24px}
.tag{left:536px;top:1871px;width:137px;height:49px;background:var(--button);color:#fff;font-size:30px;display:flex;align-items:center;justify-content:center}
.benefit .t{font-family:'Playfair Display',serif;font-size:24px;color:var(--ink)}
.benefit .d{font-size:13.5px;line-height:24px;width:290px;margin-top:4px}

/* recipes */
.recipes{top:2345px;left:0;width:1200px;height:452px;background:linear-gradient(180deg,#4a2e1c 0%,#3c2415 60%,#5a3a24 100%)}
.recipes h2{left:113px;top:40px;font-family:'Playfair Display',serif;font-weight:400;font-size:26px;color:#fff}
.recipes .sub{left:113px;top:85px;font-size:15px;color:#fff}
.ring-social{position:absolute;width:42px;height:42px;border-radius:50%;border:2px solid #e8c9a8}
.explore{left:852px;top:85px;width:215px;height:46px;border-radius:23px;background:var(--accent);font-size:14px}
.recipe{position:absolute;top:225px;width:237px;height:163px;border:3px solid #fff}

/* reviews */
.reviews{top:2797px;left:0;width:1200px;height:522px;background:linear-gradient(180deg,#f4f3f1,#ecebe8)}
.review{position:absolute;background:#fff;border:1px solid #e2e2e2;border-radius:12px;box-shadow:0 3px 10px rgba(0,0,0,.06)}
.review p{font-family:'Montserrat',sans-serif;color:var(--ink)}
.review .who{font-family:'Montserrat',sans-serif;color:var(--accent);text-transform:uppercase}
.review .place{font-family:'Montserrat',sans-serif;color:var(--accent)}
.review .arrow{position:absolute;width:16px;height:16px;background:#fff;border-right:1px solid #e2e2e2;border-bottom:1px solid #e2e2e2;transform:rotate(45deg)}
.dot{position:absolute;top:3252px;width:9px;height:9px;border-radius:50%;background:#c9c9c9}

/* footer */
.footer{top:3319px;left:0;width:1200px;height:498px;background:var(--footer)}
.footer h4{position:absolute;font-family:'Yesteryear',cursive;font-weight:400;font-size:38px;color:#fff}
.footer .line{position:absolute;display:flex;align-items:center;gap:10px;font-family:'Montserrat',sans-serif;font-size:15px;color:#fff}
.blog-thumb{position:absolute;width:82px;height:70px}
.blog-text{position:absolute;width:205px;font-family:'Montserrat',sans-serif;font-size:13.5px;line-height:21px;color:#fff}
.field{position:absolute;left:779px;width:304px;background:var(--field);border:1px solid #4a4a4a;font-family:'Montserrat',sans-serif;font-size:14px;color:#c8c8c8;padding:10px 14px}
.flinks{position:absolute;left:114px;font-family:'Montserrat',sans-serif;font-size:15px;color:#fff}
.copy{position:absolute;left:114px;top:3757px;font-family:'Montserrat',sans-serif;font-size:12.5px;color:var(--accent)}
</style>
</head>
<body>

<!-- top bar -->
<div class="abs topbar">
  <span class="abs mail">info@rtwgourmet.com</span>
  <div class="abs links"><span>Blog</span><span>FAQ</span><span>News</span><span>Order Now</span></div>
  <div class="abs socials" aria-label="Social links"><i></i><i></i><i></i><i></i></div>
</div>

<!-- header -->
<div class="abs header">
  <div class="abs brand">RTW Gourmet Mushrooms</div>
  <div class="abs nav">
    <span class="active">Home</span><span>About Us</span><span>Varieties</span><span>Recipes</span><span>Contact</span>
  </div>
  <div class="abs cart">
    <span class="ring">
      <svg width="18" height="16" viewBox="0 0 18 16" fill="none" stroke="#fff" stroke-width="1.6"><path d="M1 1h3l2 9h9l2-6H5"/><circle cx="7" cy="14" r="1.2"/><circle cx="14" cy="14" r="1.2"/></svg>
    </span>
    Cart (0)
  </div>
</div>

<!-- hero -->
<div class="abs hero" role="img" aria-label="Close-up of sautéed brown mushrooms with fresh parsley">
  <h1>Gourmet Mushroom</h1>
</div>
<div class="abs down">
  <svg width="28" height="16" viewBox="0 0 28 16" fill="none" stroke="#fff" stroke-width="3"><path d="M3 3l11 10 11-10"/></svg>
</div>

<!-- about -->
<div class="abs script about-kicker">About Us</div>
<div class="abs serif-head about-title">We are fresh oyester musroom sellers</div>
<p class="abs about-text">The goal is to attract local buyers of fresh mushrooms and to both local and international buyers freeze dried mushrooms. Mushrooms grown will be oyster mushrooms (yellow, pink, blue, king), shiitake, lions main, chestnut, and more. My business will also be selling grow kits that help families who would like to grow there own mushrooms.</p>

<div class="member">
  <div class="abs photo" style="left:127px;top:831px" role="img" aria-label="Portrait of Peter Lindqvist"></div>
  <div class="abs name" style="left:357px;top:842px">Peter Lindqvist</div>
  <p class="abs desc" style="left:357px;top:882px">The goal is to attract local buyers of fresh mushrooms and to both local and international</p>
  <div class="btn" style="left:358px;top:963px;width:119px;height:38px">LEARN MORE</div>
</div>
<div class="member">
  <div class="abs photo" style="left:624px;top:831px" role="img" aria-label="Portrait of Moira Dunstable"></div>
  <div class="abs name" style="left:853px;top:842px">Moira Dunstable</div>
  <p class="abs desc" style="left:853px;top:882px">The goal is to attract local buyers of fresh mushrooms and to both local and international</p>
  <div class="btn" style="left:855px;top:963px;width:119px;height:38px">LEARN MORE</div>
</div>
<div class="abs deco" style="left:1059px;top:942px;width:141px;height:154px;border-radius:60% 0 0 0" role="img" aria-label="Engraved illustration of a single mushroom"></div>

<!-- varieties -->
<div class="abs varieties" role="img" aria-label="Dark wooden table with a mushroom pizza in the background">
  <div class="abs script kicker">We Sell</div>
  <div class="abs serif-head title">Farm Fresh Varieties</div>

  <div class="variety" style="left:145px;top:178px"><div class="pic" style="background:linear-gradient(160deg,#8a6a55,#3e2a1e)" role="img" aria-label="King brown mushrooms"></div><div class="label">King Brown</div></div>
  <div class="variety" style="left:383px;top:178px"><div class="pic" style="background:linear-gradient(160deg,#f1d34a,#b88a1a)" role="img" aria-label="Yellow oyster mushrooms"></div><div class="label">Yellow Oyster</div></div>
  <div class="variety" style="left:613px;top:178px"><div class="pic" style="background:linear-gradient(160deg,#f1a79a,#c8604f)" role="img" aria-label="Pink oyster mushrooms"></div><div class="label">Pink Oyster</div></div>
  <div class="variety" style="left:842px;top:178px"><div class="pic" style="background:linear-gradient(160deg,#6f8fa6,#2c4357)" role="img" aria-label="Blue oyster mushrooms"></div><div class="label">Blue Oyster</div></div>

  <div class="variety" style="left:135px;top:412px"><div class="pic" style="background:linear-gradient(160deg,#8a5a3a,#e8dccb)" role="img" aria-label="Shiitake mushrooms"></div><div class="label">Shiitake</div></div>
  <div class="variety" style="left:361px;top:412px"><div class="pic" style="border-radius:50%;background:radial-gradient(circle,#fbf3e2,#e2cfa8)" role="img" aria-label="Lions mane mushroom"></div><div class="label">Lions Mane</div></div>
  <div class="variety" style="left:591px;top:412px"><div class="pic" style="background:linear-gradient(160deg,#d98a3a,#7a4a22)" role="img" aria-label="Chestnut oyster mushrooms"></div><div class="label">Chestnut Oyster</div></div>
  <div class="variety" style="left:822px;top:412px"><div class="pic" style="background:linear-gradient(160deg,#ffffff,#cfc7b8 70%,#6fa34a)" role="img" aria-label="White oyster mushrooms with greens"></div><div class="label">White Oyster</div></div>
</div>

<!-- benefits -->
<div class="abs deco" style="left:1015px;top:1776px;width:185px;height:209px;border-radius:0 0 0 100px;background:linear-gradient(150deg,#f5efe6,#d8c6ae 70%,#4f8a34)" role="img" aria-label="Sliced white mushrooms with parsley in a bowl"></div>

<div class="abs prep-card">
  <div class="abs script kicker">Methods of Preservation</div>
  <h3 class="abs serif-head">How do We Prepare ?</h3>
  <p class="abs">Lorem Ipsum is simply dummy text of the printing and typesetting industry. since the 1500s,when an unknown printer took a galley of type and scrambled it to make a type specimen book. It has survived not only five centuries, but also the leap into electronic typesettingdard dummy text ever since the 1500s,when an unknown printer took.</p>
  <div class="btn" style="left:30px;top:307px;width:119px;height:37px">LEARN MORE</div>
</div>
<div class="abs script tag">Benefits</div>

<div class="benefit">
  <svg class="abs" style="left:628px;top:1953px" width="62" height="62" viewBox="0 0 62 62" fill="none" stroke="#c4895c" stroke-width="2"><circle cx="31" cy="31" r="27" stroke-dasharray="6 3"/><circle cx="31" cy="31" r="17"/><path d="M23 31l6 6 11-12"/></svg>
  <div class="abs t" style="left:714px;top:1950px">100% Fresh Quality</div>
  <p class="abs d" style="left:717px;top:1986px">Lorem Ipsum is simply dummy text of the printing and typesetting industry.</p>
</div>
<div class="benefit">
  <svg class="abs" style="left:630px;top:2063px" width="62" height="62" viewBox="0 0 62 62" fill="none" stroke="#c4895c" stroke-width="2"><path d="M8 30c0-12 10-22 22-22s22 10 22 22z"/><path d="M24 30v22h14V30"/><path d="M6 56h50"/></svg>
  <div class="abs t" style="left:717px;top:2060px">Wide Varieties</div>
  <p class="abs d" style="left:717px;top:2096px">Pinter took a galley of type and scrambled it to make a type specimen book.</p>
</div>
<div class="benefit">
  <svg class="abs" style="left:634px;top:2172px" width="62" height="62" viewBox="0 0 62 62" fill="none" stroke="#c4895c" stroke-width="2"><path d="M6 34h50c0 12-11 20-25 20S6 46 6 34z"/><path d="M10 56h42"/><circle cx="24" cy="16" r="4"/><circle cx="36" cy="12" r="4"/><circle cx="32" cy="24" r="3"/></svg>
  <div class="abs t" style="left:717px;top:2170px">Yummy Taste</div>
  <p class="abs d" style="left:719px;top:2206px">But also the leap into electronic type setting dummy text ever since the 1500.</p>
</div>

<!-- recipes -->
<div class="abs recipes" role="img" aria-label="Dark wooden surface with herbs and spices">
  <h2 class="abs">Get Inspired Our Recipes</h2>
  <p class="abs sub">Follow us on social media, explore the website, or check out our fungi-friendly recipes.</p>
  <span class="ring-social" style="left:114px;top:124px" aria-label="Social link"></span>
  <span class="ring-social" style="left:167px;top:124px" aria-label="Social link"></span>
  <span class="ring-social" style="left:220px;top:124px" aria-label="Social link"></span>
  <span class="ring-social" style="left:275px;top:124px" aria-label="Social link"></span>
  <div class="btn explore">EXPLORE OUR RECIPES</div>

  <svg class="abs" style="left:44px;top:297px" width="42" height="20" viewBox="0 0 42 20" fill="none" stroke="#d9a071" stroke-width="2.5"><path d="M40 10H3M11 2L3 10l8 8"/></svg>
  <div class="recipe" style="left:99px;background:linear-gradient(160deg,#d9d2c8,#7a5a3f)" role="img" aria-label="Chef plating a mushroom dish"></div>
  <div class="recipe" style="left:354px;background:linear-gradient(160deg,#4a5a3a,#b8642e 60%,#2d2d2d)" role="img" aria-label="Bowls of roasted mushrooms and greens"></div>
  <div class="recipe" style="left:609px;background:linear-gradient(160deg,#c0342a,#d2a040 40%,#8a5a2a)" role="img" aria-label="Pasta with mushrooms and vegetables"></div>
  <div class="recipe" style="left:864px;background:linear-gradient(160deg,#3a3a36,#8a8578 50%,#1e1e1c)" role="img" aria-label="Stuffed mushrooms on a grill"></div>
  <svg class="abs" style="left:1118px;top:297px" width="42" height="20" viewBox="0 0 42 20" fill="none" stroke="#d9a071" stroke-width="2.5"><path d="M2 10h37M31 2l8 8-8 8"/></svg>
</div>

<!-- reviews -->
<div class="abs reviews">
  <div class="abs" style="left:0;top:400px;width:145px;height:122px;border-radius:0 90px 0 0;background:radial-gradient(circle at 30% 40%,#e9dccb,#6a5a3a 60%,#2a2a2a)" role="img" aria-label="Bowl of mushroom risotto"></div>
  <div class="abs" style="left:760px;top:0;width:440px;height:522px;background:linear-gradient(200deg,rgba(126,160,90,.55) 0%,rgba(240,235,225,0) 40%,rgba(232,220,200,.8) 80%)" role="img" aria-label="Fresh herbs and white mushrooms on a table"></div>
  <div class="abs script" style="left:0;top:56px;width:1200px;text-align:center;font-size:32px;color:#8f8a86">Reviews</div>
  <div class="abs serif-head" style="left:0;top:92px;width:1200px;text-align:center;font-size:32px">Happy Clients</div>
</div>

<div class="review" style="left:141px;top:2975px;width:238px;height:181px">
  <p style="position:absolute;left:30px;top:24px;width:190px;font-size:12.5px;line-height:21px">Nemo enim ipsam voluptatem quia voluptas sit aspernatur aut odit aut fugit, sed quia consequuntu</p>
  <div class="who" style="position:absolute;left:30px;top:128px;font-size:12.5px">Nadia Rowe</div>
  <div class="place" style="position:absolute;left:30px;top:150px;font-size:12.5px">California</div>
  <svg style="position:absolute;left:188px;top:136px" width="36" height="20" viewBox="0 0 36 20" fill="#c4895c"><circle cx="9" cy="8" r="7"/><path d="M3 10l4 10 6-8z"/><circle cx="27" cy="8" r="7"/><path d="M21 10l4 10 6-8z"/></svg>
  <span class="arrow" style="left:111px;top:172px"></span>
</div>
<div class="review" style="left:421px;top:2965px;width:357px;height:229px">
  <p style="position:absolute;left:28px;top:28px;width:310px;font-size:14.5px;line-height:25px">Nemo enim ipsam voluptatem quia voluptas sit aspernatur aut odit aut fugit, sed quia consequuntur magni dolores eos qui ratione voluptatem sequi nesciunt.</p>
  <div class="who" style="position:absolute;left:28px;top:164px;font-size:14px">Owen Pratt</div>
  <div class="place" style="position:absolute;left:28px;top:188px;font-size:14px">California</div>
  <svg style="position:absolute;left:283px;top:172px" width="40" height="22" viewBox="0 0 36 20" fill="#c4895c"><circle cx="9" cy="8" r="7"/><path d="M3 10l4 10 6-8z"/><circle cx="27" cy="8" r="7"/><path d="M21 10l4 10 6-8z"/></svg>
  <span class="arrow" style="left:170px;top:220px"></span>
</div>
<div class="review" style="left:819px;top:2975px;width:239px;height:181px">
  <p style="position:absolute;left:30px;top:24px;width:190px;font-size:12.5px;line-height:21px">Nemo enim ipsam voluptatem quia voluptas sit aspernatur aut odit aut fugit, sed quia consequuntu</p>
  <div class="who" style="position:absolute;left:30px;top:128px;font-size:12.5px">Lena Voss</div>
  <div class="place" style="position:absolute;left:30px;top:150px;font-size:12.5px">New Jercy</div>
  <svg style="position:absolute;left:188px;top:136px" width="36" height="20" viewBox="0 0 36 20" fill="#c4895c"><circle cx="9" cy="8" r="7"/><path d="M3 10l4 10 6-8z"/><circle cx="27" cy="8" r="7"/><path d="M21 10l4 10 6-8z"/></svg>
  <span class="arrow" style="left:111px;top:172px"></span>
</div>
<span class="dot" style="left:552px;background:var(--accent)"></span>
<span class="dot" style="left:573px"></span>
<span class="dot" style="left:594px"></span>
<span class="dot" style="left:615px"></span>
<span class="dot" style="left:636px"></span>

<!-- footer -->
<div class="abs footer">
  <h4 style="left:118px;top:52px">Contact</h4>
  <div class="line" style="left:114px;top:114px">
    <svg width="14" height="14" viewBox="0 0 14 14" fill="#c4895c"><path d="M3 1l2 3-1 2c1 2 2 3 4 4l2-1 3 2-1 2C6 14 0 8 1 2z"/></svg>555-014-2290</div>
  <div class="line" style="left:114px;top:143px">
    <svg width="14" height="12" viewBox="0 0 14 12" fill="#c4895c"><path d="M0 4l7-4 7 4v8H0z"/></svg>info@rtwgourmet.com</div>
  <div class="line" style="left:114px;top:172px">
    <svg width="14" height="14" viewBox="0 0 14 14" fill="#c4895c"><path d="M7 0a5 5 0 015 5c0 4-5 9-5 9S2 9 2 5a5 5 0 015-5zm0 3a2 2 0 100 4 2 2 0 000-4z"/></svg>2217 Alder Ridge Rd,</div>
  <div class="line" style="left:138px;top:201px">Brookfield WA 98000</div>

  <h4 style="left:397px;top:52px">Latest Blog</h4>
  <div class="blog-thumb" style="left:397px;top:109px;background:radial-gradient(circle,#f3efe6,#3a86b8)" role="img" aria-label="White mushrooms in a blue bowl"></div>
  <p class="blog-text" style="left:498px;top:112px">For general enquiries please email us and we'll get back to you as soon as we can.</p>
  <div class="blog-thumb" style="left:397px;top:200px;background:radial-gradient(circle,#c0302a,#e8d6a8 60%,#fff)" role="img" aria-label="Pasta dish with tomato sauce"></div>
  <p class="blog-text" style="left:496px;top:201px">For general enquiries please email us and we'll get back to you as soon as we can.</p>

  <h4 style="left:779px;top:52px">Feedback Form</h4>
</div>
<div class="field" style="top:3441px;height:38px">Name</div>
<div class="field" style="top:3493px;height:38px">Email</div>
<div class="field" style="top:3545px;height:37px">Phone</div>
<div class="field" style="top:3597px;height:96px">Message</div>
<div class="btn" style="left:779px;top:3708px;width:138px;height:43px;font-size:19px;font-weight:500">SUBMIT</div>

<div class="flinks" style="top:3675px">Home &nbsp;|&nbsp; About Us &nbsp;|&nbsp; Varieties &nbsp;|&nbsp; Recipes &nbsp;|&nbsp; Contact Us &nbsp;|&nbsp; Blog &nbsp;|&nbsp; FAQ</div>
<div class="flinks" style="top:3705px">Terms and Conditions &nbsp;|&nbsp; Privacy Policy</div>
<div class="copy">RTW Gourmet Mushrooms @ 2020. All Rights Reserved.</div>
<div class="abs" style="left:1098px;top:3660px;width:180px;height:180px;border-radius:50%;background:radial-gradient(circle,#d9c49a,#8a6a3a 60%,#e8dcc4)" role="img" aria-label="Plate of mushroom salad"></div>

</body>
</html>
```